(3) Image Sliders for Wordpress Site

We need to update our WP slides on a corporate website. We are an IP communications solution provider to government and enterprises. Our website is www.quorvex.com. You can see the existing sliders for size. I like crisp, professional-looking slides (NOT like the ones currently displayed). They shouldn't look like stock art/photos --- they should look original. They should also use current/new artistic methods (i.e. the "latest" concepts in design).

The Images should be JPG format, 946 x 376.

Use colors from logo on website, but don't completely restrict yourself. Photos are OK.

Slide Text:
Slide 1:
Main Message: "Creative solutions for government"
Bulleted text (use any kind of bullet or separator you want):
-Reduce FTE costs and eliminate capital expenses
-Dramatically improve community services
-Make government accessible for all constituents on all devices

Slide 2:
Main Message: "Brightmesh Systems Deployment"
-Take advantage of dramatic cost savings vs. going direct
-Leverage Quorvex's 13 years of experience
-Deploy On-Premises for optimal security, control and customization

Slide 3:
Main Message: "Enterprise Unified Communications"
-Revolutionize the way your people communicate and collaborate
-Realize instant cost savings by replacing multiple systems with one unified platform
-Bring everyone together, no matter where they are.
Updates

Hi Everyone I appreciate your submissions, but they are full of stock graphics and stuff I could have done..Looking for something more creative and unique to us. Since we're primarily a government/enterprise contractor, it doesn't have to be artsy or cute, but it does need to rise above the typical stock stuff i'm seeing. More information: -The Brightmesh Systems logo should go on the Brightmesh Systems-related slide -If you need more relevant logos or images let me know. Here are some slides that I like: http://plomaquad.com/images/2014/0710-1/unslider.jpg http://plomaquad.com/images/2014/0710-1/superslides.jpg http://www.tavrelkits.com/wp-content/uploads/2012/02/jquerysliders10b.jpg something like this with layered text for our gov slider, but NYC skyline: http://www.tavrelkits.com/wp-content/uploads/2012/02/jquerysliders18.jpg

Reason: Would like to see more original designs. However, we are still considering designs that have already been submitted.

Industry/Entity Type

Communications

```html
<!DOCTYPE html>
<html lang="en">
<head>
<meta charset="utf-8">
<title>Creative Solutions for Government – Slider Concepts</title>
<link rel="stylesheet" href="https://fonts.googleapis.com/css2?family=Raleway:wght@200;300&family=Open+Sans:wght@300;400;600&family=Montserrat:wght@800&display=swap">
<style>
  :root {
    --page: #ffffff;
    --white: #ffffff;
    --lime: #8dc21f;
    --charcoal-top: #3c3d40;
    --charcoal-bottom: #2a2b2d;
    --steel-top: #4f7fae;
    --steel-bottom: #2b5d93;
    --slate-top: #6c6d6f;
    --slate-bottom: #4a4b4d;
    --cobalt: #1463bd;
    --dot-dim: rgba(255,255,255,0.45);
    --rule: rgba(255,255,255,0.35);
  }
  * { box-sizing: border-box; margin: 0; padding: 0; }
  html, body {
    width: 977px; height: 1200px; overflow: hidden;
    background: var(--page);
  }
  .slider-set {
    position: absolute; left: 16px; top: 19px; width: 946px;
  }
  .slide {
    position: absolute; left: 0; width: 946px; height: 376px; overflow: hidden;
    color: var(--white);
  }
  .slide--dusk { top: 0; }
  .slide--civic { top: 393px; }
  .slide--tower { top: 786px; }

  .slide__photo { position: absolute; inset: 0; }
  .slide--dusk .slide__photo {
    background:
      radial-gradient(ellipse 30% 55% at 40% 75%, rgba(120,115,105,0.35), transparent 70%),
      linear-gradient(180deg, var(--charcoal-top), var(--charcoal-bottom));
  }
  .slide--civic .slide__photo {
    background:
      radial-gradient(ellipse 30% 55% at 40% 75%, rgba(140,175,215,0.35), transparent 70%),
      linear-gradient(180deg, var(--steel-top), var(--steel-bottom));
  }
  .slide--tower .slide__photo {
    background:
      radial-gradient(ellipse 25% 50% at 25% 85%, rgba(40,40,42,0.45), transparent 70%),
      radial-gradient(ellipse 20% 60% at 90% 40%, rgba(40,40,42,0.45), transparent 70%),
      linear-gradient(180deg, var(--slate-top), var(--slate-bottom));
  }

  .headline-light {
    position: absolute; left: 53px;
    font-family: "Raleway", sans-serif; font-weight: 200;
    font-size: 40px; line-height: 1; letter-spacing: 0.2px; white-space: nowrap;
  }
  .slide--dusk .headline-light { top: 84px; color: var(--lime); }
  .slide--civic .headline-light { top: 91px; color: var(--white); }

  .benefits {
    position: absolute; list-style: none;
    font-family: "Open Sans", sans-serif; font-weight: 300;
  }
  .benefits li { display: flex; align-items: center; white-space: nowrap; }
  .benefits svg { flex: none; }

  .slide--dusk .benefits, .slide--civic .benefits { left: 54px; font-size: 18px; }
  .slide--dusk .benefits { top: 143px; }
  .slide--dusk .benefits li { height: 30px; }
  .slide--dusk .benefits svg { margin-right: 9px; }

  .slide--civic .benefits { top: 151px; width: 626px; }
  .slide--civic .benefits li { height: 30px; }
  .slide--civic .benefits li + li { border-top: 1px solid var(--rule); }
  .slide--civic .benefits svg { margin-right: 9px; }

  .cta-outline {
    position: absolute; left: 57px; top: 259px; width: 154px; height: 36px;
    border: 1px solid var(--white);
    font-family: "Open Sans", sans-serif; font-weight: 400; font-size: 16px;
    display: flex; align-items: center; justify-content: center;
  }
  .cta-ribbon {
    position: absolute; left: 57px; top: 270px; width: 153px; height: 36px;
  }
  .cta-ribbon span {
    position: absolute; left: 28px; top: 0; line-height: 36px;
    font-family: "Open Sans", sans-serif; font-size: 16px;
  }

  .pager-arrows { position: absolute; left: 829px; top: 337px; }
  .pager-dots {
    position: absolute; display: flex; gap: 3px;
  }
  .pager-dots i {
    display: block; width: 10px; height: 10px; border-radius: 50%;
    background: var(--dot-dim);
  }
  .pager-dots i:first-child { background: var(--white); }
  .slide--dusk .pager-dots, .slide--civic .pager-dots { left: 884px; top: 339px; }
  .slide--tower .pager-dots { left: 27px; top: 33px; }

  .headline-bold {
    position: absolute; left: 366px; top: 76px;
    border-left: 4px solid var(--lime); padding-left: 13px;
    font-family: "Montserrat", sans-serif; font-weight: 800;
    font-size: 47px; line-height: 50px; letter-spacing: -2.2px; text-transform: uppercase;
    white-space: nowrap;
  }
  .slide--tower .benefits { left: 361px; top: 185px; font-size: 16px; font-weight: 400; }
  .slide--tower .benefits li { height: 30px; }
  .slide--tower .benefits svg { margin-right: 5px; }
  .cta-pill {
    position: absolute; left: 359px; top: 287px; width: 146px; height: 35px;
    border-radius: 18px; background: var(--cobalt);
    border: 1px solid rgba(255,255,255,0.35);
    font-family: "Open Sans", sans-serif; font-weight: 600; font-size: 16px;
    display: flex; align-items: center; justify-content: center;
  }
</style>
</head>
<body>
<div class="slider-set">

  <section class="slide slide--dusk">
    <div class="slide__photo" role="img" aria-label="Domed civic building between Parisian apartment blocks under a stormy sky, darkened"></div>
    <h1 class="headline-light">Creative Solutions for Government</h1>
    <ul class="benefits">
      <li><svg width="17" height="17" viewBox="0 0 17 17"><circle cx="8.5" cy="8.5" r="7.3" fill="none" stroke="#fff" stroke-width="1.5"/><circle cx="8.5" cy="8.5" r="3.4" fill="#fff"/></svg>Reduce FTE costs and eliminate capital expenses</li>
      <li><svg width="17" height="17" viewBox="0 0 17 17"><circle cx="8.5" cy="8.5" r="7.3" fill="none" stroke="#fff" stroke-width="1.5"/><circle cx="8.5" cy="8.5" r="3.4" fill="#fff"/></svg>Dramatically improve community services</li>
      <li><svg width="17" height="17" viewBox="0 0 17 17"><circle cx="8.5" cy="8.5" r="7.3" fill="none" stroke="#fff" stroke-width="1.5"/><circle cx="8.5" cy="8.5" r="3.4" fill="#fff"/></svg>Make government accessible for all constituents on all devices</li>
    </ul>
    <div class="cta-outline">Call to Action</div>
    <svg class="pager-arrows" width="36" height="14" viewBox="0 0 36 14"><path d="M8 1 L2 7 L8 13" fill="none" stroke="#fff" stroke-width="2.5"/><path d="M23 1 L29 7 L23 13" fill="none" stroke="#fff" stroke-width="2.5"/></svg>
    <div class="pager-dots"><i></i><i></i><i></i></div>
  </section>

  <section class="slide slide--civic">
    <div class="slide__photo" role="img" aria-label="Domed civic building between Parisian apartment blocks, tinted blue"></div>
    <h1 class="headline-light">Creative Solutions for Government</h1>
    <ul class="benefits">
      <li><svg width="17" height="17" viewBox="0 0 17 17"><circle cx="8.5" cy="8.5" r="7.3" fill="none" stroke="#fff" stroke-width="1.5"/><path d="M4.8 8.6 L7.6 11.3 L12.6 5.4" fill="none" stroke="#fff" stroke-width="1.7"/></svg>Reduce FTE costs and eliminate capital expenses</li>
      <li><svg width="17" height="17" viewBox="0 0 17 17"><circle cx="8.5" cy="8.5" r="7.3" fill="none" stroke="#fff" stroke-width="1.5"/><path d="M4.8 8.6 L7.6 11.3 L12.6 5.4" fill="none" stroke="#fff" stroke-width="1.7"/></svg>Dramatically improve community services</li>
      <li><svg width="17" height="17" viewBox="0 0 17 17"><circle cx="8.5" cy="8.5" r="7.3" fill="none" stroke="#fff" stroke-width="1.5"/><path d="M4.8 8.6 L7.6 11.3 L12.6 5.4" fill="none" stroke="#fff" stroke-width="1.7"/></svg>Make government accessible for all constituents on all devices</li>
    </ul>
    <div class="cta-ribbon">
      <svg width="153" height="36" viewBox="0 0 153 36"><polygon points="0,0 153,0 142,18 153,36 0,36" fill="#8dc21f"/></svg>
      <span>Call to Action</span>
    </div>
    <svg class="pager-arrows" width="36" height="14" viewBox="0 0 36 14"><path d="M8 1 L2 7 L8 13" fill="none" stroke="#fff" stroke-width="2.5"/><path d="M23 1 L29 7 L23 13" fill="none" stroke="#fff" stroke-width="2.5"/></svg>
    <div class="pager-dots"><i></i><i></i><i></i></div>
  </section>

  <section class="slide slide--tower">
    <div class="slide__photo" role="img" aria-label="Upward view of tall office towers against an overcast sky, grey toned"></div>
    <div class="pager-dots"><i></i><i></i><i></i></div>
    <h1 class="headline-bold">Creative Solutions<br>for Government</h1>
    <ul class="benefits">
      <li><svg width="18" height="18" viewBox="0 0 18 18"><circle cx="9" cy="9" r="8.2" fill="#e9e9e9" stroke="#fff" stroke-width="1"/><path d="M5 9.2 L8 12 L13.2 6" fill="none" stroke="#5a5b5d" stroke-width="2"/></svg>Reduce FTE costs and eliminate capital expenses</li>
      <li><svg width="18" height="18" viewBox="0 0 18 18"><circle cx="9" cy="9" r="8.2" fill="#e9e9e9" stroke="#fff" stroke-width="1"/><path d="M5 9.2 L8 12 L13.2 6" fill="none" stroke="#5a5b5d" stroke-width="2"/></svg>Dramatically improve community services</li>
      <li><svg width="18" height="18" viewBox="0 0 18 18"><circle cx="9" cy="9" r="8.2" fill="#e9e9e9" stroke="#fff" stroke-width="1"/><path d="M5 9.2 L8 12 L13.2 6" fill="none" stroke="#5a5b5d" stroke-width="2"/></svg>Make government accessible for all constituents on all devices</li>
    </ul>
    <div class="cta-pill">Call to Action</div>
  </section>

</div>
</body>
</html>
```